LeadaVigor brochure design

I would like a brochure designed for our Leadavigor program.

LeadaVigor is QMR’s flagship fitness program that combines exercise, nutrition, coaching tailored specifically to an executives’ lifestyle and customized specifically for them. LeadaVigor is designed exclusively for C-level and senior executives in the top three tiers of the organization.

The brochure should contain pertinent info such as the services offered by leadavigor, (http://www.quartzmeridianwellness.example/leadavigor-services), as well as some of the other benefits of LeadaVigor program. All of the information can be gleaned from our LeadaVigor pages (http://www.quartzmeridianwellness.example/leadavigor). Also, I would like to incorporate the pull phrase under the WHY LEADAVIGOR heading on that webpage.

I would also like to see graphics used from our website banner (http://www.quartzmeridianwellness.example/corporate-fitness)

All the details can be pulled from our website http://www.quartzmeridianwellness.example/leadavigor

Target Market(s)

Senior and C-Level executives in large to midsize companies. Owners of smaller companies.

Industry/Entity Type

Fitness

Requirements
Must have
• The brochure must use our logo (attached) It should be consistent with the look of our other brochures (please see attached detox brochure) or consistent with our shape your shield and nimbler art work (please see attached).
• It must be a tri-fold. It must have some artwork. The artwork should represent fitness for a business person. Pixvault has great images (keyword: suit, dumbbell).
Nice to have
• May be nice to have a pic of our facility and possibly a pic of me the owner. Please see attached.

```html
<!DOCTYPE html>
<html lang="en">
<head>
<meta charset="utf-8">
<title>LeadaVigor Brochure</title>
<link rel="stylesheet" href="https://fonts.googleapis.com/css2?family=Lato:wght@400;700&family=Oswald:wght@600;700&display=swap">
<style>
  :root {
    --canvas-dark: #2f2f31;
    --canvas-mid: #3b3b3e;
    --navy: #27306a;
    --navy-deep: #1b2252;
    --brand-blue: #1c5eae;
    --band-blue: #1d64c0;
    --band-deep: #0d3f88;
    --panel-grey: #a9a9aa;
    --panel-edge: #8a8a8c;
    --silver: #d6d7da;
    --ink: #111111;
    --white: #ffffff;
  }
  * { box-sizing: border-box; margin: 0; padding: 0; }
  html, body { width: 1200px; height: 848px; overflow: hidden; }
  body { background: var(--canvas-dark); font-family: "Lato", Arial, sans-serif; }

  .brochure {
    position: relative; width: 1200px; height: 848px; overflow: hidden;
    background: radial-gradient(ellipse at 50% 45%, var(--canvas-mid) 0%, var(--canvas-dark) 70%);
  }

  /* Header band */
  .header-band {
    position: absolute; left: 0; top: 0; width: 1200px; height: 72px;
    background: var(--navy);
  }
  .header-bar {
    position: absolute; left: 0; top: 17px; width: 1192px; height: 33px;
    background: var(--silver);
  }
  .header-title {
    position: absolute; right: 40px; top: 17px; line-height: 33px;
    font-weight: 400; font-size: 26px; color: var(--navy-deep); letter-spacing: 0.5px;
  }

  /* Connecting bands */
  .connector { position: absolute; height: 14px; background: var(--band-blue); }
  .connector.thin { height: 6px; background: var(--band-deep); }

  /* Hero */
  .hero {
    position: absolute; left: 4px; top: 81px; width: 822px; height: 200px;
    background: var(--white);
  }
  .hero-title {
    position: absolute; left: 18px; top: 8px;
    font-size: 66px; font-weight: 400; line-height: 1; color: var(--ink);
  }
  .hero-lede {
    position: absolute; left: 20px; top: 93px;
    font-size: 17.5px; line-height: 23px; color: var(--ink); white-space: nowrap;
  }
  .hero-photo {
    position: absolute; left: 440px; top: 0; width: 382px; height: 200px;
    background: linear-gradient(90deg, #ffffff 0%, #e9e9ea 35%, #cfd0d3 60%, #f4f4f4 100%);
  }

  /* Panels */
  .panel { position: absolute; }
  .panel::before {
    content: ""; position: absolute; inset: 6px;
    background: radial-gradient(ellipse at 50% 50%, var(--panel-grey) 60%, var(--panel-edge) 100%);
    filter: blur(6px);
  }
  .panel > * { position: absolute; }
  .panel-heading { color: var(--brand-blue); font-size: 17px; font-weight: 400; line-height: 23px; }
  .panel-text { color: var(--ink); font-size: 18.5px; line-height: 24px; white-space: nowrap; }

  .panel-team { left: 50px; top: 313px; width: 300px; height: 465px; }
  .panel-team .panel-heading { left: 0; width: 300px; top: 32px; text-align: center; }
  .team-trait {
    left: 7px; width: 286px; height: 44px;
    display: flex; align-items: center; justify-content: center;
    background: radial-gradient(ellipse at 50% 50%, #3c3c3e 30%, #6a6a6d 70%, rgba(140,140,142,0) 100%);
    font-family: "Oswald", Impact, sans-serif; font-weight: 700; font-size: 20px;
    color: var(--white); letter-spacing: 0.3px;
  }

  .panel-why { left: 456px; top: 313px; width: 314px; height: 515px; }
  .panel-why .panel-heading { left: 34px; top: 76px; }
  .panel-why .panel-text { left: 34px; }

  .panel-profit { left: 866px; top: 81px; width: 296px; height: 718px; }
  .panel-profit .panel-heading { left: 44px; top: 46px; white-space: nowrap; }
  .profit-item {
    left: 44px; font-size: 15.5px; line-height: 21px; color: var(--ink); white-space: nowrap;
  }

  .owner-photo {
    position: absolute; left: 880px; top: 668px; width: 250px; height: 138px;
    background: radial-gradient(ellipse at 50% 65%, #2f58b8 0%, #1d3d8a 45%, rgba(60,60,62,0) 80%);
  }
  .owner-caption {
    position: absolute; left: 866px; top: 808px; width: 290px; text-align: center;
    font-family: "Oswald", Impact, sans-serif; font-weight: 600; font-size: 17px;
    color: var(--white); letter-spacing: 0.3px;
  }
</style>
</head>
<body>
<main class="brochure">
  <header class="header-band">
    <div class="header-bar"></div>
    <div class="header-title">LEADAVIGOR</div>
  </header>

  <div class="connector" style="left:0;top:420px;width:56px"></div>
  <div class="connector thin" style="left:0;top:440px;width:56px"></div>
  <div class="connector" style="left:344px;top:420px;width:118px"></div>
  <div class="connector thin" style="left:344px;top:440px;width:118px"></div>
  <div class="connector" style="left:764px;top:500px;width:108px"></div>
  <div class="connector thin" style="left:764px;top:520px;width:108px"></div>
  <div class="connector" style="left:1156px;top:320px;width:44px"></div>
  <div class="connector thin" style="left:1156px;top:340px;width:44px"></div>

  <section class="hero">
    <h1 class="hero-title">LEADAVIGOR</h1>
    <p class="hero-lede">QMR's LeadaVigor will get your executives healthier,<br>happier, and ultimately more productive in as<br>little as 4 1/2 hours of exercise a week!</p>
    <div class="hero-photo" role="img" aria-label="Executive in a white shirt and dark tie lifting a dumbbell"></div>
  </section>

  <section class="panel panel-team">
    <h2 class="panel-heading">WHO ARE WE?</h2>
    <div class="team-trait" style="top:86px">FORMER ATHLETES</div>
    <div class="team-trait" style="top:166px">KNOWLEDGEABLE</div>
    <div class="team-trait" style="top:246px">CONFIDENT COACHES</div>
    <div class="team-trait" style="top:326px">GREAT MOTIVATORS</div>
    <div class="team-trait" style="top:403px">ROLE MODELS</div>
  </section>

  <section class="panel panel-why">
    <h2 class="panel-heading">WHY EXECUTIVE&nbsp; WELLNESS</h2>
    <p class="panel-text" style="top:124px">An increase in BMI is directly<br>related to absenteeism and<br>health care costs.</p>
    <p class="panel-text" style="top:221px">Every $1.00 spent on wellness<br>leads to:<br>$3.27 less on health care costs.<br>$2.73 less on absenteeism</p>
    <p class="panel-text" style="top:342px">Unfit employees are less<br>productive.</p>
  </section>

  <section class="panel panel-profit">
    <h2 class="panel-heading">IMPROVE YOUR COMPANY'S<br>&nbsp;PROFITS</h2>
    <p class="profit-item" style="top:116px">The benefits below are well<br>established and will ultimately<br>boost your company's success:</p>
    <p class="profit-item" style="top:199px">Reduced absenteeism</p>
    <p class="profit-item" style="top:240px">Reduced health care costs</p>
    <p class="profit-item" style="top:281px">Increased retention</p>
    <p class="profit-item" style="top:322px">Increased productivity</p>
    <p class="profit-item" style="top:363px">Improved morale, recruiting<br>and company image</p>
    <p class="profit-item" style="top:425px">Increases the bottom line</p>
  </section>

  <div class="owner-photo" role="img" aria-label="Portrait of the owner in a blue athletic shirt with arms crossed"></div>
  <div class="owner-caption">MARCUS DELVANE - OWNER</div>
</main>
</body>
</html>
```